Flyer für Freiwillige Feuerwehr
Zielgruppe
Freiwillige Feuerwehr/ Es soll zum einen die Jungen von 10 Jahren bis 16 sowie Erwachse von 16 Jahren bis open end Angesprochen werden
Aufgabenstellung
Es sollen zum einen die Erwachsenen und die Jugend auf einen Flyer geschickt angesprochen werden. Zum einen können wir mit dem Flyer die Kinder fangen und wenn die Eltern von den Kindern bzw. Erwachsene das lesen, dann könnten auch Sie angesprochen werden.
Inhalt für die Erwachsenen noch nicht Mitglieder:
Der Flyer sollte Verantwortung, Kameradschaft und eine gute berufliche oder ehrenamtliche Entwicklung betonen. Es geht hier um die Werbung von Personen, die bereit sind, sich aktiv in der Feuerwehr zu engagieren.
o Hauptaussage: 'Engagiere dich – Deine Feuerwehr braucht dich!' Möchtest du nur zusehen oder live dabei sein?!
o Visuelle Gestaltung: Zeige Bilder von aktiven Feuerwehrleuten im Einsatz, bei Einsätzen oder Trainings. Zeige Professionalität und Teamarbeit.
o Benefits: Überzeuge mit Aspekten wie Weiterbildungsmöglichkeiten, Teamarbeit, Verantwortung und gesellschaftlicher Beitrag.
o Call to Action (CTA): 'Mach den nächsten Schritt – Werde aktives Mitglied der Feuerwehr!'
o Kontaktinformationen: Eine einfache Möglichkeit zur Kontaktaufnahme, z.B. Telefonnummer für einen persönlichen Kontakt, E-Mail-Adresse oder QR-Code für Online-Anmeldung.
Inhalt für die Jugend:
Der Flyer muss ansprechend, modern und dynamisch sein, um Jugendliche zu motivieren. Junge Menschen interessieren sich oft für Abenteuer, Teamarbeit und den Beitrag zur Gemeinschaft.
• Hauptaussage: 'Werde Teil unseres Teams und erlebe spannende Abenteuer!'
• Visuelle Gestaltung: Bilder von jungen Feuerwehrmitgliedern in Aktion (z.B. Übungseinsätze, Abenteuer, Teamwork). Eine starke, klare Headline, z.B. 'Feuerwehr – Deine Chance für Action und Teamgeist!'
• Benefits: Betone, was die Jugend davon hat: Spaß, Herausforderungen, neue Freunde, Teilnahme an Übungen und Veranstaltungen.
• Call to Action (CTA): 'Komm zu uns! Wir suchen dich – Melde dich noch heute an!'
• Kontaktinfo..

```html
<!DOCTYPE html>
<html lang="en">
<head>
<meta charset="utf-8">
<title>Get Involved – Fire Service Recruitment Flyer</title>
<link href="https://fonts.googleapis.com/css2?family=Archivo:wght@700;800;900&family=Roboto:wght@400;500&display=swap" rel="stylesheet">
<style>
  :root {
    --navy: #1b2d47;
    --yellow: #dbe14a;
    --yellow-deep: #ccd13a;
    --backdrop: #e8e8e8;
    --photo-top: #e9dcd6;
    --photo-bottom: #2a3548;
  }
  * { margin: 0; padding: 0; box-sizing: border-box; }
  html, body {
    width: 1200px; height: 916px; overflow: hidden;
    background: var(--backdrop);
  }
  .flyer {
    position: absolute; left: 296px; top: 27px;
    width: 607px; height: 862px;
    background: linear-gradient(180deg, var(--yellow) 40%, var(--yellow-deep) 100%);
    overflow: hidden;
    font-family: "Roboto", Arial, sans-serif;
    color: var(--navy);
  }
  .hero-photo {
    position: absolute; left: 0; top: 0; width: 607px; height: 350px;
    background: linear-gradient(180deg, var(--photo-top) 0%, #d9c3c6 35%, #55607a 65%, var(--photo-bottom) 100%);
  }
  .headline-band {
    position: absolute; left: 0; top: 376px; width: 607px; height: 94px;
    background: var(--navy);
  }
  .headline-notch { position: absolute; left: 283px; top: 375px; }
  .headline {
    position: absolute; left: 0; top: 376px; width: 607px; height: 94px;
    display: flex; align-items: center; justify-content: center;
    font-family: "Archivo", Arial, sans-serif; font-weight: 900;
    font-size: 71px; letter-spacing: 0.5px; color: var(--yellow);
    padding-top: 4px;
  }
  .subheadline {
    position: absolute; left: 0; top: 470px; width: 607px; height: 54px;
    display: flex; align-items: center; justify-content: center;
    font-family: "Archivo", Arial, sans-serif; font-weight: 900;
    font-size: 33px; color: var(--navy);
  }
  .tagline {
    position: absolute; left: 0; top: 524px; width: 607px; height: 22px;
    background: var(--navy); color: var(--yellow);
    font-size: 17px; text-align: center; line-height: 22px;
  }
  .benefits {
    position: absolute; left: 26px; top: 565px; width: 555px; height: 151px;
    border: 3px solid var(--navy);
  }
  .benefits-header {
    height: 35px; background: var(--navy);
    display: flex; align-items: center; justify-content: center; gap: 22px;
  }
  .benefits-rule { width: 158px; height: 2px; background: var(--yellow); }
  .benefits-title {
    font-family: "Archivo", Arial, sans-serif; font-weight: 800;
    font-size: 28px; color: var(--yellow);
  }
  .benefit {
    position: absolute; font-size: 10px; white-space: nowrap;
    display: flex; align-items: center; gap: 7px;
  }
  .benefit::before {
    content: ""; width: 6px; height: 6px; border-radius: 50%; background: var(--navy);
  }
  .cta-block { position: absolute; top: 736px; height: 58px; background: var(--navy); }
  .cta-block.left { left: 0; width: 145px; }
  .cta-block.right { left: 482px; width: 125px; }
  .cta {
    position: absolute; left: 145px; top: 736px; width: 337px; height: 58px;
    text-align: center;
  }
  .cta-title {
    font-family: "Archivo", Arial, sans-serif; font-weight: 800;
    font-size: 29px; line-height: 34px; padding-top: 2px;
  }
  .cta-text { font-size: 15px; line-height: 18px; }
  .phone {
    position: absolute; left: 177px; top: 806px; width: 251px; height: 34px;
    background: var(--navy); color: var(--yellow);
    font-family: "Archivo", Arial, sans-serif; font-weight: 800; font-size: 26px;
    display: flex; align-items: center; justify-content: center;
  }
</style>
</head>
<body>
  <main class="flyer">
    <div class="hero-photo" role="img" aria-label="Photo of four young firefighters in helmets and reflective gear stacking hands in front of a blossoming tree"></div>

    <div class="headline-band"></div>
    <svg class="headline-notch" width="42" height="20" viewBox="0 0 42 20" aria-hidden="true">
      <polygon points="0,0 42,0 21,20" fill="#dbe14a"/>
    </svg>
    <h1 class="headline">GET INVOLVED</h1>
    <h2 class="subheadline">YOUR FIRE SERVICE NEEDS YOU!</h2>
    <p class="tagline">Do you just want to watch or be there live?!</p>

    <section class="benefits">
      <div class="benefits-header">
        <span class="benefits-rule"></span>
        <h3 class="benefits-title">BENEFITS</h3>
        <span class="benefits-rule"></span>
      </div>
      <span class="benefit" style="left:17px; top:72px;">Training and Development Opportunities</span>
      <span class="benefit" style="left:235px; top:72px;">Community Impact</span>
      <span class="benefit" style="left:359px; top:72px;">Teamwork and Camaraderie</span>
      <span class="benefit" style="left:102px; top:107px;">Compensation and Benefits</span>
      <span class="benefit" style="left:309px; top:107px;">Responsibilities and Leadership</span>
    </section>

    <div class="cta-block left"></div>
    <div class="cta-block right"></div>
    <div class="cta">
      <p class="cta-title">TAKE THE NEXT STEP</p>
      <p class="cta-text">Become an active member of the fire service!</p>
    </div>

    <p class="phone">+ 1234567890</p>
  </main>
</body>
</html>
```